Website Home Page for Women's Health Medical Office

Redesign existing homepage for website using existing logo. Current website location is www.lumawomenscare.com. Please give it a modern, streamlined, playful feel.

Please give it a feminine feel and make it bright and cheerful using logo colors.

Target Market(s)

Women between the ages of 25-45

Industry/Entity Type

Medical Office

Coding

Coded - Design and coding required

Number of Pages Required

1 page

Font styles to use
Sans Serif
Other font styles liked:
• SEGOI UI script for text and GIL SANS for bold (or their equivilent)

Colors
E54698
E96AAD
F1A4CE
F9D9EA
FCEFF6

Requirements
Must have
• Existing logo. Logo Colors. Feminine, cheerful, simple design. all relevant contact information
Nice to have
• clean lines and streamlined look
Should not have
• Cluttered

```html
<!DOCTYPE html>
<html lang="en">
<head>
<meta charset="utf-8">
<title>Luma OB/GYN – Bellmont, CA</title>
<link href="https://fonts.googleapis.com/css2?family=Kanit:wght@500;600&family=Maven+Pro:wght@400;500;600;700&display=swap" rel="stylesheet">
<style>
:root{
  --pink:#e54698;
  --pink-mid:#e96aad;
  --pink-soft:#f1a4ce;
  --pink-pale:#f9d9ea;
  --pink-mist:#fcf0f6;
  --navy:#3c4562;
  --navy-deep:#2b3149;
  --ink:#3a3f4f;
  --text:#5b6070;
  --white:#ffffff;
}
*{margin:0;padding:0;box-sizing:border-box}
html,body{width:1200px;height:4700px;overflow:hidden}
body{position:relative;background:var(--white);font-family:"Maven Pro",sans-serif;color:var(--text)}
.abs{position:absolute}
svg.band{position:absolute;left:0;display:block}

/* header */
.topbar{top:0;left:0;width:1200px;height:64px}
.topbar-contact{top:18px;left:655px;display:flex;gap:30px;align-items:center;color:var(--white);font-size:15px;font-weight:600;white-space:nowrap}
.topbar-contact span{display:flex;align-items:center;gap:8px}
.topbar-contact .sep{width:2px;height:18px;background:rgba(255,255,255,.8)}
.brand{top:78px;left:88px;display:flex;align-items:center;gap:16px;white-space:nowrap}
.brand-mark{width:54px;height:54px;border-radius:50%;background:var(--pink)}
.brand-name{font-family:"Maven Pro",sans-serif;font-weight:700;font-size:38px;color:var(--ink)}
.nav{top:118px;left:601px;display:flex;gap:28px;font-size:15px;font-weight:600;color:var(--ink);letter-spacing:.3px;white-space:nowrap}
.header-rule{top:183px;left:0;width:1200px;height:7px;background:#c9ccd4}

/* hero */
.hero-photo{top:190px;left:0;width:1200px;height:510px;background:linear-gradient(100deg,#e9edf1 0%,#dfe5eb 45%,#c9d6df 68%,#aebfcb 100%)}
.hero-welcome{top:270px;left:88px;font-size:33px;font-weight:500;color:var(--ink);white-space:nowrap}
.hero-title{top:320px;left:88px;padding:4px 10px 6px;background:rgba(170,175,190,.45);font-family:"Kanit",sans-serif;font-weight:600;font-size:32px;color:var(--pink);white-space:nowrap}
.hero-copy{top:405px;left:88px;width:510px;font-size:14px;line-height:26px;color:var(--text)}
.btn{display:flex;align-items:center;justify-content:center;background:var(--navy);color:var(--white);border-radius:26px;font-weight:600;font-size:14px;white-space:nowrap}
.hero-btn{top:505px;left:146px;width:208px;height:45px}

/* split sections */
.frame{border:16px solid var(--pink);box-shadow:0 4px 10px rgba(0,0,0,.18)}
.photo{position:absolute}
.eyebrow{display:flex;align-items:center;gap:12px;font-size:16px;font-weight:600;letter-spacing:4px;color:var(--pink-soft);white-space:nowrap}
.eyebrow i{display:block;flex:1;height:5px;background:var(--pink-soft)}
.sec-heading{font-family:"Kanit",sans-serif;font-weight:500;font-size:31px;line-height:36px;color:var(--ink);margin:10px 0 14px}
.sec-copy p{font-size:13.5px;line-height:24px;color:var(--text);margin-bottom:20px}

/* accepting band */
.accept{top:1440px;left:60px;width:566px;text-align:center;color:var(--white)}
.accept .kicker{font-size:21px;letter-spacing:4px;font-weight:500}
.accept h2{font-family:"Kanit",sans-serif;font-weight:600;font-size:32px;margin-top:10px;white-space:nowrap}
.accept .btn{width:206px;height:45px;margin:14px auto 0}
.accept .or{margin-top:12px;font-size:14px;letter-spacing:3px;font-weight:600}
.accept .call{margin-top:4px;font-size:15px;letter-spacing:2px;font-weight:600}
.card-white{background:var(--white);box-shadow:0 4px 14px rgba(0,0,0,.15)}

/* help section */
.help-head{top:2486px;left:88px;color:var(--white);white-space:nowrap}
.help-head h2{font-family:"Kanit",sans-serif;font-weight:600;font-size:34px}
.help-head p{font-size:22px;letter-spacing:4px;margin-top:2px}
.service-card{position:absolute;width:444px;height:635px}
.service-card .u{position:absolute;border:13px solid var(--pink);border-bottom:none;height:85px}
.service-card h3{position:absolute;font-weight:500;font-size:31px;line-height:38px;color:var(--ink);white-space:nowrap}
.service-card p{position:absolute;font-size:13.5px;line-height:28px;color:var(--text);width:400px}
.service-card .btn{position:absolute;width:208px;height:46px}

/* footer */
.footer{top:4027px;left:0;width:1200px;height:593px;background:var(--navy)}
.news-title{top:4094px;left:0;width:1200px;text-align:center;color:var(--white);font-size:31px;font-weight:500}
.news-sub{top:4138px;left:0;width:1200px;text-align:center;color:#e4e6ee;font-size:14px;font-weight:500}
.news-form{top:4177px;left:394px;display:flex}
.news-input{width:334px;height:42px;background:var(--white);font-size:13px;color:#b9bcc6;padding:13px 20px}
.news-submit{width:80px;height:42px;background:var(--pink);color:var(--white);font-size:14px;font-weight:600;display:flex;align-items:center;justify-content:center}
.footer-rule{top:4280px;left:88px;width:1028px;height:1px;background:#5a6380}
.f-brand{top:4350px;left:88px;color:var(--white);font-weight:700;font-size:30px;white-space:nowrap}
.f-tag{top:4437px;left:88px;color:#e4e6ee;font-size:14px;white-space:nowrap}
.f-head{color:var(--white);font-size:15px;font-weight:700;letter-spacing:.5px;white-space:nowrap}
.f-head::after{content:"";display:block;width:22px;height:3px;background:var(--pink);margin-top:8px}
.f-links{list-style:none;font-size:15px;color:#c8ccd8;white-space:nowrap}
.f-links li{height:37.5px}
.f-contact li{display:flex;gap:14px;align-items:flex-start}
.f-contact svg{flex:none;margin-top:2px}
.socials{top:4534px;left:88px;display:flex;gap:7px}
.socials span{width:28px;height:28px;border:2px solid var(--pink);border-radius:50%}
.copy-bar{top:4620px;left:0;width:1200px;height:80px;background:var(--navy-deep);color:#7f869e;font-size:13px;text-align:center;line-height:80px}
</style>
</head>
<body>

<!-- header -->
<svg class="band topbar" width="1200" height="64" viewBox="0 0 1200 64"><polygon points="530,0 1200,0 1200,64 600,64" fill="var(--pink)"/></svg>
<div class="abs topbar-contact">
  <span><svg width="16" height="16" viewBox="0 0 24 24"><path d="M6.6 10.8a15 15 0 0 0 6.6 6.6l2.2-2.2a1 1 0 0 1 1-.25 11.4 11.4 0 0 0 3.6.57 1 1 0 0 1 1 1V20a1 1 0 0 1-1 1A17 17 0 0 1 3 4a1 1 0 0 1 1-1h3.5a1 1 0 0 1 1 1c0 1.25.2 2.45.57 3.57a1 1 0 0 1-.25 1z" fill="#fff"/></svg>(555) 014-2270</span>
  <i class="sep"></i>
  <span><svg width="18" height="14" viewBox="0 0 18 14"><rect x="1" y="1" width="16" height="12" rx="1" fill="none" stroke="#fff" stroke-width="2"/><path d="M1 1l8 6 8-6" fill="none" stroke="#fff" stroke-width="2"/></svg>admin@lumawomenscare.com</span>
</div>
<div class="abs brand"><span class="brand-mark"></span><span class="brand-name">Luma OB/GYN</span></div>
<nav class="abs nav"><span>HOME</span><span>SERICES</span><span>RESOURCES</span><span>ABOUT US</span><span>CONTACT US</span></nav>
<div class="abs header-rule"></div>

<!-- hero -->
<div class="abs hero-photo" role="img" aria-label="Photo of a doctor in a white coat holding a stethoscope"></div>
<div class="abs hero-welcome">Welcome to</div>
<div class="abs hero-title">Luma OB/GYN, Bellmont, CA</div>
<p class="abs hero-copy">Luma OB/GYN offers you the best care possible in a personalized setting. We are currently accepting patients. Call our office now to make an appointment.</p>
<div class="abs btn hero-btn">Make Appointment</div>
<svg class="band" style="top:580px" width="1200" height="125" viewBox="0 0 1200 125"><polygon points="0,12 1200,92 1200,125 0,125" fill="#fff"/><polygon points="0,32 1200,110 1200,125 0,125" fill="var(--pink)"/><polygon points="0,125 1200,110 1200,125" fill="#fff"/></svg>

<!-- about -->
<div class="abs frame" style="top:788px;left:279px;width:244px;height:476px"></div>
<div class="photo" style="top:828px;left:88px;width:397px;height:394px;background:linear-gradient(135deg,#4b556b,#2f3448 60%,#3d4866)" role="img" aria-label="Portrait of a smiling physician in navy scrubs"></div>
<div class="abs" style="top:786px;left:600px;width:516px">
  <div class="eyebrow">ABOUT US<i></i></div>
  <h2 class="sec-heading">Serving bellmont springs medical center</h2>
  <div class="sec-copy">
    <p>At Luma OB/GYN in Bellmont, California, we believe better health starts when the patient is educated. For this reason, we take time to listen to our patients concerns, explain each option available, and to answer any questions our patients may have so that they can make informed decisions.</p>
    <p>At Luma OB/GYN, our providers tailor every procedure performed and treatment option recommended to meet the specific needs of our patients.</p>
    <p>We remain up-to-date on the latest technology and practice guidelines for women's health.</p>
    <p>Our medical providers will take time to give you the personalized health care you deserve. This includes taking time to listen to you and screening you for problems to help ensure that any health issues are diagnosed and treated as early as possible.</p>
  </div>
</div>

<!-- accepting band -->
<svg class="band" style="top:1298px" width="1200" height="431" viewBox="0 0 1200 431"><polygon points="0,110 1200,0 1200,344 0,431" fill="var(--pink)"/></svg>
<div class="abs accept">
  <div class="kicker">Better Health Starts Here!</div>
  <h2>NOW ACCEPTING NEW PATIENTS</h2>
  <div class="btn">Make Appointment</div>
  <div class="or">OR</div>
  <div class="call">Call Us: (555) 014-2270</div>
</div>
<div class="abs card-white" style="top:1372px;left:730px;width:386px;height:452px"></div>
<div class="abs" style="top:1394px;left:751px;width:362px;height:408px;border:16px solid var(--pink)"></div>
<div class="photo" style="top:1417px;left:775px;width:316px;height:363px;background:linear-gradient(160deg,#f4f1ef,#e6e2df 55%,#d9d7d9)" role="img" aria-label="Photo of a young doctor with a stethoscope, arms crossed"></div>

<!-- services intro -->
<div class="abs frame" style="top:1873px;left:279px;width:244px;height:480px"></div>
<div class="photo" style="top:1917px;left:88px;width:392px;height:390px;background:linear-gradient(135deg,#c9c2b3,#8fa7b0 55%,#7c97a2)" role="img" aria-label="Photo of a nurse in scrubs holding a newborn baby"></div>
<div class="abs" style="top:1866px;left:600px;width:518px">
  <div class="eyebrow">OUR SERVICES<i></i></div>
  <h2 class="sec-heading">Your OB/GYN specialist</h2>
  <div class="sec-copy">
    <p>Luma OB/GYN offers you the best care possible in a personalized setting. We are currently accepting patients. Call our office now to make an appointment.</p>
    <p>Luma OB/GYN (located near Bellmont Springs Hospital in Bellmont, CA) is a medical office that specializes in Christ-centered healthcare for women of all ages. Our team of exclusively female providers have years of experience taking care of women with a variety of pregnancy and gynecology concerns.</p>
    <p>Whether you need a routine examination, help during your pregnancy, have questions on birth control, or another female concern, we offer the best care possible for our patients. That is why better health starts here.</p>
    <p>Our office provides you with an environment where you can feel comfortable and where you know you will be in good hands. Our providers are leaders women's health. Dr. Harlow is a board certified obstetrician and gynecologist. Dr. Ortega is a board eligible obstetrician and gynecologist.</p>
  </div>
</div>

<!-- help band -->
<svg class="band" style="top:2398px" width="1200" height="430" viewBox="0 0 1200 430"><polygon points="0,0 1200,56 1200,430 0,312" fill="var(--pink)"/></svg>
<div class="abs help-head"><h2>HOW CAN WE HELP YOU?</h2><p>Health Services Offered</p></div>

<div class="abs card-white" style="top:2603px;left:157px;width:888px;height:635px"></div>
<div class="abs card-white" style="top:3274px;left:157px;width:888px;height:635px"></div>

<div class="service-card" style="top:2603px;left:157px">
  <div class="u" style="top:12px;left:13px;width:397px"></div>
  <div class="photo" style="top:40px;left:40px;width:345px;height:241px;background:linear-gradient(120deg,#e9ecef,#cdd8de 50%,#b7c3c8)" role="img" aria-label="Photo of a doctor greeting a pregnant patient"></div>
  <h3 style="top:302px;left:40px">Pregnancy care</h3>
  <p style="top:360px;left:40px">Receiving regular care in pregnancy is important for the health of both you and your baby. Our obstetricians work with you every step of the way during your pregnancy and delivery to make sure your individual needs are met and co ensure this special journey is a memorable one.</p>
  <div class="btn" style="top:547px;left:107px">Learn More</div>
</div>
<div class="service-card" style="top:2603px;left:622px">
  <div class="u" style="top:12px;left:13px;width:397px"></div>
  <div class="photo" style="top:40px;left:40px;width:345px;height:241px;background:linear-gradient(120deg,#8a5c3a,#c99b78 50%,#e6d3c4)" role="img" aria-label="Photo of hands holding a blister pack of birth control pills"></div>
  <h3 style="top:302px;left:40px">Birth control</h3>
  <p style="top:360px;left:25px;width:410px">Our gynecologists are knowledgeable on all forms of birth control including the IUD, the arm implant, vaginal ring insertion, birth control pills, and more! We would love to work with you to determine the best option for you and your lifestyle.</p>
  <div class="btn" style="top:547px;left:107px">Learn More</div>
</div>
<div class="service-card" style="top:3274px;left:157px">
  <div class="u" style="top:12px;left:13px;width:397px"></div>
  <div class="photo" style="top:48px;left:40px;width:345px;height:242px;background:linear-gradient(120deg,#d9d4cf,#6b6f85 50%,#2f3650)" role="img" aria-label="Photo of a woman working at a laptop"></div>
  <h3 style="top:308px;left:40px">Well women exams</h3>
  <p style="top:367px;left:40px">Our providers will help you to stay healthy by performing a physical exam on you annually. We will screen you for multiple health conditions that may pose a risk to you. This includes screening you for cancerous conditions of the breast, ovaries and cervix.</p>
  <div class="btn" style="top:556px;left:107px">Learn more</div>
</div>
<div class="service-card" style="top:3274px;left:622px">
  <div class="u" style="top:12px;left:13px;width:397px"></div>
  <div class="photo" style="top:48px;left:40px;width:345px;height:242px;background:linear-gradient(160deg,#f1ece8,#e7d3c8 50%,#b99c96)" role="img" aria-label="Photo of a woman holding a paper smile card over her abdomen"></div>
  <h3 style="top:308px;left:40px">Women's health</h3>
  <p style="top:367px;left:40px">Whether you are dealing with painful or irregular periods, fibroids, or other women's health issues, we can help. We offer a variety of the most up-to-date treatment options to help you regain your lifestyle.</p>
  <div class="btn" style="top:556px;left:107px">Learn more</div>
</div>

<!-- footer -->
<svg class="band" style="top:3949px" width="1200" height="80" viewBox="0 0 1200 80"><polygon points="0,0 1200,40 1200,80 0,80" fill="var(--pink)"/></svg>
<div class="abs footer"></div>
<div class="abs news-title">Newsletter</div>
<div class="abs news-sub">Subscribe to our newsletter to receive news and updated</div>
<div class="abs news-form"><div class="news-input">Enter your email address</div><div class="news-submit">Submit</div></div>
<div class="abs footer-rule"></div>

<div class="abs f-brand">Luma OB/GYN</div>
<div class="abs f-tag">Serving bellmont springs medical center</div>
<div class="abs f-head" style="top:4490px;left:88px">SOCIAL MEDIA</div>
<div class="abs socials"><span aria-label="Social profile"></span><span aria-label="Social profile"></span><span aria-label="Social profile"></span></div>

<div class="abs" style="top:4358px;left:489px">
  <div class="f-head">SITE LINKS</div>
  <ul class="f-links" style="margin-top:32px"><li>Home</li><li>Services</li><li>About Us</li><li>News</li></ul>
</div>
<div class="abs" style="top:4358px;left:669px">
  <div class="f-head">COMPANY</div>
  <ul class="f-links" style="margin-top:32px"><li>Terms of use</li><li>Privacy</li><li>Contact us</li><li>Sitemap</li></ul>
</div>
<div class="abs" style="top:4358px;left:846px">
  <div class="f-head">CONTACT</div>
  <ul class="f-links f-contact" style="margin-top:32px">
    <li><svg width="14" height="14" viewBox="0 0 24 24"><path d="M6.6 10.8a15 15 0 0 0 6.6 6.6l2.2-2.2a1 1 0 0 1 1-.25 11.4 11.4 0 0 0 3.6.57 1 1 0 0 1 1 1V20a1 1 0 0 1-1 1A17 17 0 0 1 3 4a1 1 0 0 1 1-1h3.5a1 1 0 0 1 1 1c0 1.25.2 2.45.57 3.57a1 1 0 0 1-.25 1z" fill="#e54698"/></svg>(555) 014-2270</li>
    <li><svg width="14" height="12" viewBox="0 0 18 14"><rect x="1" y="1" width="16" height="12" rx="1" fill="#e54698"/><path d="M1 1l8 6 8-6" fill="none" stroke="#3c4562" stroke-width="1.5"/></svg>admin@lumawomenscare.com</li>
    <li><svg width="14" height="14" viewBox="0 0 14 14"><rect x="2" y="1" width="10" height="12" rx="1" fill="#e54698"/><rect x="4" y="3" width="6" height="3" fill="#3c4562"/></svg>555-014-2283</li>
    <li style="height:auto;line-height:24px"><svg width="14" height="16" viewBox="0 0 24 28"><path d="M12 0a10 10 0 0 0-10 10c0 7.5 10 18 10 18s10-10.5 10-18A10 10 0 0 0 12 0zm0 14a4 4 0 1 1 0-8 4 4 0 0 1 0 8z" fill="#e54698"/></svg><span>1480 Willow Crest Avenue,<br>Suite 210, Bellmont, CA 95012</span></li>
  </ul>
</div>

<div class="abs copy-bar">Copyright © 2022 www.lumawomenscare.com</div>

</body>
</html>
```